Brochure Cover and Back pages

We are a US-based cosmetics company that sells state-of-the-art skin care products, including advanced anti-aging serums, natural mineral sunscreens, organic antioxidant moisturizers, and organic face cleansers. We need a product brochure. We already have chosen a design for the layout of the product info pages. But we still need a cover page and a back page. We are looking for simple but elegant design for the cover page. The back page is less important and we already know what we want on the back page. It will be the company's mission statement and at the bottom, the company URL, phone number, etc.

The brochure has two folds. So there will be three panels on both sides. The size of each panel is 16.5 (l) x 9.5 (w) cm.

At the end of the project, we expect the designer to integrate all the pages so that the finished copy is read to be sent off to a printing service for printing.

All the product info pages are attached. Also attached are the text (info) to go on the back page, company logo with and without the tagline, the icon in the logo.

YOu are welcome to visit our website www.corvanyx.com to learn about our products.

Industry/Entity Type

Cosmetics

```html
<!DOCTYPE html>
<html lang="en">
<head>
<meta charset="utf-8">
<title>Corvanyx Brochure – Cover and Back Panels</title>
<link rel="stylesheet" href="https://fonts.googleapis.com/css2?family=Tinos:wght@400;700&family=Kalam:wght@700&family=Didact+Gothic&display=swap">
<style>
  :root {
    --page-bg: #ebe7e2;
    --ink: #2a2626;
    --ink-soft: #3b3737;
    --divider: #55504f;
    --veil: rgba(255, 255, 255, 0.74);
    --badge: rgba(120, 120, 124, 0.62);
    --blush: #f7c7bd;
    --photo-light: #eef3f4;
    --photo-skin: #e9d3c6;
    --photo-mint: #bfe0dc;
    --photo-mist: #d9e7e8;
  }
  * { box-sizing: border-box; margin: 0; padding: 0; }
  html, body {
    width: 1200px; height: 733px; overflow: hidden;
    background: var(--page-bg);
  }
  .brochure {
    position: absolute; left: 30px; top: 36px;
    width: 1140px; height: 661px;
    overflow: hidden;
  }
  .brochure__photo {
    position: absolute; inset: 0;
    background:
      radial-gradient(ellipse 360px 220px at 640px 330px, var(--photo-skin), transparent 70%),
      radial-gradient(ellipse 320px 200px at 900px 380px, var(--photo-skin), transparent 70%),
      linear-gradient(100deg, var(--photo-light) 0%, var(--photo-mist) 40%, var(--photo-mint) 70%, var(--photo-mist) 100%);
  }
  .panel {
    position: absolute; top: 0; width: 380px; height: 661px;
  }
  .panel--about { left: 0; background: var(--veil); }
  .panel--contact { left: 380px; border-left: 2px solid var(--divider); }
  .panel--cover { left: 760px; border-left: 2px solid var(--divider); }

  .about {
    font-family: "Tinos", "Times New Roman", serif;
    color: var(--ink-soft);
    text-align: center;
    padding: 22px 30px 0;
    font-size: 13px;
    line-height: 22px;
  }
  .about__title {
    font-size: 18px; font-weight: 700; text-decoration: underline;
    margin-bottom: 20px; color: var(--ink);
  }
  .about__heading {
    font-size: 17px; font-weight: 700; color: var(--ink);
    margin-bottom: 6px;
  }
  .about__intro { margin-bottom: 14px; }
  .mission-list { list-style: none; margin-bottom: 20px; }
  .mission-list li::before { content: "• "; }

  .brand-badge {
    position: absolute; left: 85px; top: 45px;
    width: 206px; height: 206px; border-radius: 50%;
    background: var(--badge);
    display: flex; align-items: center; justify-content: center;
    font-family: "Tinos", "Times New Roman", serif;
    font-weight: 700; font-size: 34px; color: var(--blush);
  }
  .contact {
    position: absolute; left: 0; right: 0; bottom: 22px;
    font-family: "Didact Gothic", "Helvetica", sans-serif;
    color: var(--ink); text-align: center;
    font-size: 15px; line-height: 17px; letter-spacing: 0.5px;
  }
  .contact__row { position: relative; display: inline-block; }
  .contact__icon {
    position: absolute; left: -22px; top: 1px; width: 15px; height: 15px;
  }
  .contact__block { margin-bottom: 8px; }

  .cover__name {
    position: absolute; left: 0; right: 0; top: 98px;
    text-align: center;
    font-family: "Tinos", "Times New Roman", serif;
    font-weight: 700; font-size: 78px; color: var(--ink);
    letter-spacing: -1px;
  }
  .cover__tagline {
    position: absolute; left: 0; right: 0; top: 548px;
    text-align: center;
    font-family: "Kalam", "Comic Sans MS", cursive;
    font-weight: 700; font-size: 38px; line-height: 52px;
    color: var(--ink);
  }
</style>
</head>
<body>
  <main class="brochure">
    <div class="brochure__photo" role="img" aria-label="Soft-focus photo of hands pumping white lotion from a bottle into a palm"></div>

    <section class="panel panel--about">
      <div class="about">
        <h2 class="about__title">About Us</h2>
        <h3 class="about__heading">Who We Are</h3>
        <p class="about__intro">Corvanyx is a cosmetics company dedicated to developing high quality and high performance skin care products. Corvanyx's science-based approach promises to deliver smart skin care to consumers!</p>
        <h3 class="about__heading">Our Mission</h3>
        <ul class="mission-list">
          <li>To Create Beauty Solutions through Science</li>
          <li>To Inform and Empower Consumers</li>
          <li>To Create Beauty Solutions through Science</li>
        </ul>
        <p>Skin is one of the most, if not the most, researched organs in the human body. As a result, tremendous progress has been made over the past few decades in our understanding of the skin, its functions and various physiological processes. As science advances, we will surely learn even more about the skin and how to keep it healthy and delay its aging. For now, what science has already learned about skin care is what drives our product development work. We have made it our mission to create useful and effective skin care and beauty products based on the findings of clinical studies and scientific research.</p>
      </div>
    </section>

    <section class="panel panel--contact">
      <div class="brand-badge">Corvanyx</div>
      <address class="contact">
        <div class="contact__block">
          <span class="contact__row">
            <svg class="contact__icon" viewBox="0 0 16 16" aria-hidden="true"><path d="M8 1a5 5 0 0 0-5 5c0 3.6 5 9 5 9s5-5.4 5-9a5 5 0 0 0-5-5zm0 7a2 2 0 1 1 0-4 2 2 0 0 1 0 4z" fill="#2a2626"/></svg>2150 Larkmoor Ave. Ste. 400
          </span><br>
          Brightwater, CA 94871<br>USA
        </div>
        <div class="contact__block">
          <span class="contact__row">
            <svg class="contact__icon" viewBox="0 0 16 16" aria-hidden="true"><circle cx="8" cy="8" r="7" fill="none" stroke="#2a2626" stroke-width="1.3"/><path d="M5.6 4.2l1.4 1.6-.8 1c.5 1.1 1.3 1.9 2.4 2.4l1-.8 1.6 1.4-.9 1.3C7.6 11 5 8.4 4.3 5.1z" fill="#2a2626"/></svg>(1-855-555-0142)
          </span><br>
          1-866-555-0187<br>(925) 555-0163
        </div>
        <div>
          <span class="contact__row">
            <svg class="contact__icon" viewBox="0 0 16 16" aria-hidden="true"><g fill="none" stroke="#2a2626" stroke-width="1.2"><circle cx="8" cy="8" r="6.5"/><ellipse cx="8" cy="8" rx="3" ry="6.5"/><path d="M1.5 8h13M2.5 4.8h11M2.5 11.2h11"/></g></svg>www.corvanyx.com
          </span>
        </div>
      </address>
    </section>

    <section class="panel panel--cover">
      <h1 class="cover__name">Corvanyx</h1>
      <p class="cover__tagline">Bringing You<br>Smart Skin Care</p>
    </section>
  </main>
</body>
</html>
```